I just want a letterhead for my company. It is a construction and consulting company and it would be nice if what we do could be incorporated into the letterhead. I don't need anything fancy just something that is simple and that looks official.

If we could include the outline of townhouse into the name or something like that it would be great. I'm being asked to write at least 300 word for this description but in all honesty because I want it nice and simple I do't have much more to write so am just typing this in order to achieve the three hundred word requirement.

Target Market(s)

It is just needed for professional purposes

Industry/Entity Type

Contractor

Font styles to use
Serif
Sans Serif

Colors
3276b5

Requirements
Must have
• On the top left of the page it must have a letterhead that says RW48 Construction & Consulting Ltd. and hopefully designed in a way that shows we are a construction company. For example maybe the outline of a house or excavator is on the back ground or incorporated into the letters.

On the right hand side it must have address and contact info:
#527 - 8260 Pellworth St
Burnaby, BC
V3K 2M9
RW48Holdings@brindlemail.example
604.555.0182
Nice to have
• Somehow incorporate that this is a construction company into the design of the letterhead. Let's keep it nice, clean and simple.
Should not have
• No fancy writing or bright colours.

```html
<!DOCTYPE html>
<html lang="en">
<head>
<meta charset="utf-8">
<title>RW48 Construction &amp; Consulting Ltd. — Letterhead</title>
<link rel="stylesheet" href="https://fonts.googleapis.com/css2?family=Open+Sans:wght@400;600&display=swap">
<style>
  :root{
    --brand-blue:#1f7cc0;
    --brand-blue-light:#3a96d8;
    --accent-grey:#a9abad;
    --text-grey:#6b6d70;
    --paper:#ffffff;
    --backdrop:#d9dcdd;
  }
  *{box-sizing:border-box;margin:0;padding:0}
  html,body{width:1200px;height:784px;overflow:hidden;background:var(--backdrop)}
  body{font-family:"Open Sans",Arial,sans-serif;position:relative}

  .letterhead{
    position:absolute;left:360px;top:22px;width:480px;height:740px;
    background:var(--paper);box-shadow:0 2px 10px rgba(0,0,0,.12);
    overflow:hidden;
  }

  .corner-accent{position:absolute;width:5px;height:42px}
  .corner-accent--left{left:0}
  .corner-accent--right{right:0}
  .corner-accent--blue{top:0;background:var(--brand-blue-light)}
  .corner-accent--grey{top:46px;background:var(--accent-grey)}

  .brand{
    position:absolute;top:96px;left:0;right:0;
    display:flex;align-items:center;justify-content:center;gap:8px;
  }
  .brand__mark{width:9px;height:9px;border-radius:50%;background:var(--brand-blue);flex:none}
  .brand__name{
    font-weight:400;font-size:15px;line-height:1;color:var(--brand-blue);
    letter-spacing:.2px;white-space:nowrap;
  }

  .contact-bar{
    position:absolute;left:16px;right:16px;bottom:38px;
    display:flex;align-items:center;justify-content:center;gap:10px;
    font-style:normal;font-size:8.5px;color:var(--text-grey);white-space:nowrap;
  }
  .contact-item{display:flex;align-items:center;gap:4px}
  .contact-icon{width:10px;height:10px;flex:none}

  .footer-rule{position:absolute;left:0;right:0;bottom:0;height:26px}
  .footer-rule__thin{position:absolute;left:0;right:0;bottom:4px;height:2px;background:var(--brand-blue)}
  .footer-rule__band{position:absolute;bottom:12px;height:4px}
  .footer-rule__band--blue{left:0;width:230px;background:var(--brand-blue-light)}
  .footer-rule__band--grey{left:236px;width:110px;background:var(--accent-grey)}
  .footer-rule__band--end{left:352px;right:0;background:var(--brand-blue-light)}
</style>
</head>
<body>
  <main class="letterhead">
    <span class="corner-accent corner-accent--left corner-accent--blue"></span>
    <span class="corner-accent corner-accent--left corner-accent--grey"></span>
    <span class="corner-accent corner-accent--right corner-accent--blue"></span>
    <span class="corner-accent corner-accent--right corner-accent--grey"></span>

    <header class="brand">
      <span class="brand__mark"></span>
      <span class="brand__name">RW48 Construction &amp; Consulting Ltd.</span>
    </header>

    <footer>
      <address class="contact-bar">
        <span class="contact-item">
          <svg class="contact-icon" viewBox="0 0 10 10" aria-hidden="true"><circle cx="5" cy="5" r="5" fill="var(--brand-blue)"/><path d="M5 2.2a1.8 1.8 0 0 0-1.8 1.8C3.2 5.4 5 7.8 5 7.8S6.8 5.4 6.8 4A1.8 1.8 0 0 0 5 2.2z" fill="#fff"/><circle cx="5" cy="4" r=".6" fill="var(--brand-blue)"/></svg>
          #527 - 8260 Pellworth St Burnaby, BC V3K 2M9
        </span>
        <span class="contact-item">
          <svg class="contact-icon" viewBox="0 0 10 10" aria-hidden="true"><circle cx="5" cy="5" r="5" fill="var(--brand-blue)"/><path d="M3.3 2.6l1 1-.5.8c.3.7.9 1.3 1.6 1.6l.8-.5 1 1-.6.9C5 7.3 2.7 5 2.5 3.2z" fill="#fff"/></svg>
          604.555.0182
        </span>
        <span class="contact-item">
          <svg class="contact-icon" viewBox="0 0 10 10" aria-hidden="true"><circle cx="5" cy="5" r="5" fill="var(--brand-blue)"/><rect x="2.5" y="3.3" width="5" height="3.4" fill="#fff"/><path d="M2.5 3.3L5 5.3l2.5-2" stroke="var(--brand-blue)" stroke-width=".6" fill="none"/></svg>
          RW48Holdings@brindlemail.example
        </span>
      </address>
      <div class="footer-rule">
        <span class="footer-rule__band footer-rule__band--blue"></span>
        <span class="footer-rule__band footer-rule__band--grey"></span>
        <span class="footer-rule__band footer-rule__band--end"></span>
        <span class="footer-rule__thin"></span>
      </div>
    </footer>
  </main>
</body>
</html>
```